Business Card Design Project

Cyber Security. Company name is quietBastion.

Industry/Entity Type

Computer Security

Contact Information for Business Card

Gordon Vastrick
Founder and Chief Hacker

2184 W. Harlow Ave.
Suite 314
Chicago, IL 60689
773.555.0193
gordon.vastrick@quietbastion.example
www.quietbastion.example

```html
<!DOCTYPE html>
<html lang="en">
<head>
<meta charset="utf-8">
<title>quietBastion Business Card</title>
<link href="https://fonts.googleapis.com/css2?family=Open+Sans:wght@400&family=Roboto:ital,wght@0,400;0,500;0,700;1,500&display=swap" rel="stylesheet">
<style>
  :root {
    --backdrop: #dfe1e4;
    --card-front: #313645;
    --card-back: #6279be;
    --white: #ffffff;
    --ink-dark: #2b2f3c;
    --stripe-orange: #e8712e;
    --stripe-grey: #b9b2a8;
    --stripe-green: #5bb04a;
    --mark-tone: #8fa0d6;
  }
  * { margin: 0; padding: 0; box-sizing: border-box; }
  html, body {
    width: 1200px; height: 1197px; overflow: hidden;
    background: var(--backdrop);
  }
  .card {
    position: absolute; left: 302px; width: 572px; height: 327px;
    box-shadow: 0 18px 28px rgba(0,0,0,0.25);
  }
  .card--front { top: 181px; background: var(--card-front); }
  .card--back { top: 644px; background: var(--card-back); }

  .brand {
    position: absolute; left: 0; right: 0; top: 128px;
    display: flex; justify-content: center; align-items: center; gap: 14px;
  }
  .brand__dot {
    width: 40px; height: 40px; border-radius: 50%;
    background: var(--white);
  }
  .brand__name {
    font-family: "Open Sans", sans-serif; font-weight: 400;
    font-size: 50px; line-height: 1; color: var(--white);
    letter-spacing: -0.5px;
  }

  .stripes { position: absolute; top: 278px; width: 150px; }
  .stripes--left { left: 0; }
  .stripes--right { right: 0; }
  .stripe { height: 4px; margin-bottom: 5px; }
  .stripe--orange { background: var(--stripe-orange); }
  .stripe--grey { background: var(--stripe-grey); }
  .stripe--green { background: var(--stripe-green); }

  .website {
    position: absolute; left: 0; right: 0; top: 280px; text-align: center;
    font-family: "Roboto", sans-serif; font-weight: 500;
    font-size: 19px; color: var(--white); letter-spacing: 0.3px;
  }

  .back-mark {
    position: absolute; left: 70px; top: 62px;
    width: 140px; height: 200px; border-radius: 50%;
    background: var(--mark-tone);
  }

  .person {
    position: absolute; right: 32px; top: 52px; text-align: right;
    font-family: "Roboto", sans-serif;
  }
  .person__name { font-weight: 700; font-size: 23px; color: var(--white); }
  .person__title {
    font-weight: 500; font-style: italic; font-size: 10px;
    color: var(--ink-dark); margin-top: 4px;
  }

  .contact {
    position: absolute; left: 309px; top: 156px;
    font-family: "Roboto", sans-serif; font-weight: 700;
    font-size: 11px; color: var(--white); list-style: none;
  }
  .contact__item { display: flex; align-items: flex-start; margin-bottom: 17px; }
  .contact__icon { width: 12px; height: 13px; margin-right: 16px; flex: none; }
  .contact__text { line-height: 15px; }
</style>
</head>
<body>
  <section class="card card--front">
    <div class="brand">
      <span class="brand__dot"></span>
      <span class="brand__name">quietBastion</span>
    </div>
    <div class="stripes stripes--left">
      <div class="stripe stripe--orange"></div>
      <div class="stripe stripe--grey"></div>
      <div class="stripe stripe--green"></div>
    </div>
    <div class="stripes stripes--right">
      <div class="stripe stripe--orange"></div>
      <div class="stripe stripe--grey"></div>
      <div class="stripe stripe--green"></div>
    </div>
    <p class="website">www.quietbastion.example</p>
  </section>

  <section class="card card--back">
    <div class="back-mark" role="img" aria-label="Brand symbol area"></div>
    <div class="person">
      <p class="person__name">Gordon Vastrick</p>
      <p class="person__title">Founder and Chief Hacker</p>
    </div>
    <ul class="contact">
      <li class="contact__item">
        <svg class="contact__icon" viewBox="0 0 12 13"><rect x="3" y="0.5" width="6" height="12" rx="1" fill="#2b2f3c"/><rect x="4" y="2" width="4" height="7" fill="#6279be"/></svg>
        <span class="contact__text">773.555.0193</span>
      </li>
      <li class="contact__item">
        <svg class="contact__icon" viewBox="0 0 12 13"><rect x="1" y="3" width="10" height="7" fill="none" stroke="#2b2f3c" stroke-width="1.3"/><path d="M1 3.5 L6 7 L11 3.5" fill="none" stroke="#2b2f3c" stroke-width="1.3"/></svg>
        <span class="contact__text">gordon.vastrick@quietbastion.example</span>
      </li>
      <li class="contact__item">
        <svg class="contact__icon" viewBox="0 0 12 13"><path d="M6 0.5 C3 0.5 1.5 2.6 1.5 4.6 C1.5 7.6 6 12.5 6 12.5 C6 12.5 10.5 7.6 10.5 4.6 C10.5 2.6 9 0.5 6 0.5 Z" fill="#2b2f3c"/><circle cx="6" cy="4.6" r="1.6" fill="#6279be"/></svg>
        <span class="contact__text">2184 W. Harlow Ave.<br>Suite 314<br>Chicago, IL 60689</span>
      </li>
    </ul>
  </section>
</body>
</html>
```